business card with 2 locations on 1 card

I need a modern looking business card that I would use at 2 different locations. Possibly 1 location on 1 side and other location on other side. One should be able to distinguish the 2 locations immediately before having to read the address or description on card. You can take a look at my website to see what I'm drawn to. The logo is brand new that I just purchased on Craft Hive. I want to emphasize family.
Updates

Let's not use the yellow and blue colors. Added Thursday, August 31, 2017

Target Market(s)

women and children

Industry/Entity Type

Health And Wellness

Contact Information for Business Card

Business name: Willow Brook Chiropractic & Acupuncture
My name: Lorin Daske
Job title: DC, MAOM, LAc (CA), CNS

Location 1
Address: 4817 Marlowe Blvd, Suite B-100, Frisco, TX 75034
Phone: (469) 555-0182
Fax: (972) 555-0137

Location 2
Address: 1936 Belvane Road, Suite 100, Plano, TX 75075
Phone: (469) 555-0169
Fax: (972) 555-0137

Email: drlorindaske@mailnest.example
Website: www.drlorindaske.example

Font styles to use
Serif
Sans Serif

Colors

Designer to choose colors to be used in the design.

Requirements
Must have
• distinction between 2 locations.
Nice to have
• Colors preference below is there. But I like to see what you come up with too!

```html
<!DOCTYPE html>
<html lang="en">
<head>
<meta charset="utf-8">
<title>Willow Brook Chiropractic &amp; Acupuncture – Business Cards</title>
<link rel="stylesheet" href="https://fonts.googleapis.com/css2?family=Cinzel:wght@500;600&family=Lato:wght@400;700&display=swap">
<style>
  :root {
    --teal: #2e6f6f;
    --white: #ffffff;
    --paper: #eceeed;
    --ink-grey: #5d6464;
  }
  * { box-sizing: border-box; margin: 0; padding: 0; }
  html, body { width: 1200px; height: 880px; overflow: hidden; background: var(--paper); }
  body { position: relative; font-family: "Lato", Arial, sans-serif; }

  .card {
    position: absolute;
    width: 700px;
    height: 400px;
    border-radius: 22px;
    overflow: hidden;
    box-shadow: 0 6px 18px rgba(0,0,0,.18);
  }
  .card--plano { left: 60px; top: 30px; background: var(--teal); color: var(--white); }
  .card--frisco { left: 440px; top: 450px; background: var(--white); color: var(--ink-grey); }

  .card__art { position: absolute; inset: 0; width: 700px; height: 400px; }

  .brand { position: absolute; left: 40px; top: 36px; }
  .brand__mark {
    width: 78px; height: 78px; border-radius: 50%;
    border: 4px solid currentColor; margin-left: 20px; margin-bottom: 12px;
  }
  .card--plano .brand__mark { border-color: var(--white); }
  .card--frisco .brand__mark { border-color: var(--teal); }
  .brand__name {
    font-family: "Cinzel", Georgia, serif; font-weight: 600;
    font-size: 34px; line-height: 1; letter-spacing: 1px;
  }
  .brand__tagline {
    font-family: "Cinzel", Georgia, serif; font-weight: 500;
    font-size: 12.5px; letter-spacing: 1.2px; margin-top: 4px;
  }
  .card--frisco .brand__name, .card--frisco .brand__tagline { color: var(--teal); }

  .person { position: absolute; left: 40px; top: 206px; }
  .person__name {
    font-family: "Cinzel", Georgia, serif; font-weight: 600;
    font-size: 24px; letter-spacing: 1px;
  }
  .person__title { font-size: 15px; margin-top: 2px; }

  .contact { position: absolute; left: 40px; font-size: 15.5px; line-height: 1.45; }
  .card--plano .contact { top: 264px; }
  .card--frisco .contact { top: 226px; }
  .contact__line { display: flex; align-items: center; gap: 8px; }
  .icon { width: 16px; height: 16px; flex: none; }

  .email {
    position: absolute; left: 40px; bottom: 16px;
    display: flex; align-items: center; gap: 8px; font-size: 16px;
  }
  .card--plano .email { color: var(--teal); }
  .card--frisco .email { color: var(--white); }

  .website {
    position: absolute; right: 30px; bottom: 58px; font-size: 16px; letter-spacing: .3px;
    white-space: nowrap;
  }
  .card--plano .website { color: var(--teal); }
  .card--frisco .website { color: var(--white); }
</style>
</head>
<body>

<!-- Location 2: Plano -->
<section class="card card--plano" aria-label="Plano location card">
  <svg class="card__art" viewBox="0 0 700 400">
    <polygon points="0,352 420,330 700,212 700,400 0,400" fill="#ffffff"/>
    <circle cx="560" cy="110" r="175" fill="#ffffff"/>
    <circle cx="560" cy="110" r="161" fill="#2e6f6f" role="img" aria-label="Large tree illustration area"/>
  </svg>

  <div class="brand">
    <div class="brand__mark"></div>
    <div class="brand__name">Willow Brook</div>
    <div class="brand__tagline">Chiropractic &amp; Acupuncture</div>
  </div>

  <div class="person">
    <div class="person__name">Lorin Daske</div>
    <div class="person__title">DC, MAOM, LAc (CA), CNS</div>
  </div>

  <div class="contact">
    <div class="contact__line">1936 Belvane Road, Suite 100, Plano, TX 75075</div>
    <div class="contact__line">
      <svg class="icon" viewBox="0 0 16 16"><circle cx="8" cy="8" r="7.5" fill="#fff"/><path d="M4.5 9.5h7l-1-3h-5z" fill="#2e6f6f"/></svg>
      (469) 555-0169
      <svg class="icon" viewBox="0 0 16 16"><circle cx="8" cy="8" r="7.5" fill="#fff"/><rect x="4.5" y="5" width="7" height="6" rx="1" fill="#2e6f6f"/></svg>
      (972) 555-0137
    </div>
  </div>

  <div class="email">
    <svg class="icon" viewBox="0 0 16 16"><circle cx="8" cy="8" r="7.5" fill="#2e6f6f"/><rect x="4" y="5" width="8" height="6" fill="#fff"/><path d="M4 5l4 3.5L12 5" stroke="#2e6f6f" fill="none"/></svg>
    drlorindaske@mailnest.example
  </div>
  <div class="website">www.drlorindaske.example</div>
</section>

<!-- Location 1: Frisco -->
<section class="card card--frisco" aria-label="Frisco location card">
  <svg class="card__art" viewBox="0 0 700 400">
    <polygon points="0,352 420,330 700,212 700,400 0,400" fill="#2e6f6f"/>
    <circle cx="560" cy="110" r="175" fill="#2e6f6f"/>
    <circle cx="560" cy="110" r="161" fill="#ffffff" role="img" aria-label="Large tree illustration area"/>
  </svg>

  <div class="brand">
    <div class="brand__mark"></div>
    <div class="brand__name">Willow Brook</div>
    <div class="brand__tagline">Chiropractic &amp; Acupuncture</div>
  </div>

  <div class="contact">
    <div class="contact__line">4817 Marlowe Blvd,</div>
    <div class="contact__line">Suite B-100, Frisco, TX 75034</div>
    <div class="contact__line">
      <svg class="icon" viewBox="0 0 16 16"><circle cx="8" cy="8" r="7.5" fill="#2e6f6f"/><path d="M4.5 9.5h7l-1-3h-5z" fill="#fff"/></svg>
      (469) 555-0182
    </div>
    <div class="contact__line">
      <svg class="icon" viewBox="0 0 16 16"><circle cx="8" cy="8" r="7.5" fill="#2e6f6f"/><rect x="4.5" y="5" width="7" height="6" rx="1" fill="#fff"/></svg>
      (972) 555-0137
    </div>
  </div>

  <div class="email">
    <svg class="icon" viewBox="0 0 16 16"><circle cx="8" cy="8" r="7.5" fill="#fff"/><rect x="4" y="5" width="8" height="6" fill="#2e6f6f"/><path d="M4 5l4 3.5L12 5" stroke="#fff" fill="none"/></svg>
    drlorindaske@mailnest.example
  </div>
  <div class="website">www.drlorindaske.example</div>
</section>

</body>
</html>
```